依頼詳細
ロゴはミナモワークスで作成していただいていますので、それを使用していただいきたいです。ホームページは現在作成中です。ロゴを取り入れ、柔らかい雰囲気でシンプルなイメージ、わかりやすい感じがいいです。
記載項目
病院名、ロゴ、開業日、内覧会の日程、住所、電話番号、ホームページのアドレス、診察時間、休診日 対象動物、挨拶等
サイズ
A4
ページ数
片面
希望イメージ
シンプル 複雑
単色 カラフル
暗い 明るい
日常 高級
遊び心 厳粛
未来的 伝統的
女性的 男性的
希望する色
納品ファイル
補足説明
ロゴを添付します。

挨拶内容
「はじめまして、はるかぜペットクリニック院長の森岡健司です。大学卒業後、熊本市内の動物病院で7年間勤務し、2014年3月24日に動物病院を開院することになりました。
ホームドクターとして地域の皆様に親しまれる病院であるとともに、飼い主様と一緒に家族である動物たちの最善のケアができるように努めてまいりたいと思います。ワンちゃん達が遊べるスペースも少しですが用意してあります。ぜひ気軽に遊びにいらしてください。今後ともよろしくお願い致します。」
おそくなりましたが、ホームページのドメイン決まりました。
http://harukaze-petclinic.exampleです。
よろしくお願いいたします。
■ 選んだ理由

シンプルで開院ということがわかりやすかったため。
犬の写真の雰囲気も良かったです。

■ 提案者全員のお礼・コメント

いいデザインを多数いただいてありがとうございます。それぞれおもしろくけっこう悩ませていただきました。また、よろしくお願いいたします。

```html
<!DOCTYPE html>
<html lang="ja">
<head>
<meta charset="utf-8">
<title>はるかぜペットクリニック 開院のご案内</title>
<link href="https://fonts.googleapis.com/css2?family=M+PLUS+Rounded+1c:wght@500;800&family=Noto+Sans+JP:wght@400;700&display=swap" rel="stylesheet">
<style>
:root{
  --blue:#1f6fc2;
  --blue-dark:#155aa3;
  --blue-pale:#dce8f6;
  --blue-soft:#b9cfea;
  --green:#79b82a;
  --ink:#333;
  --white:#fff;
}
*{margin:0;padding:0;box-sizing:border-box}
html,body{width:873px;height:1200px;overflow:hidden;background:var(--white)}
body{font-family:"Noto Sans JP",sans-serif;color:var(--ink)}
.flyer{position:relative;width:873px;height:1200px;overflow:hidden;background:var(--white)}
.opening-date{position:absolute;top:22px;left:0;width:100%;text-align:center;font-family:"M PLUS Rounded 1c",sans-serif;font-weight:800;font-size:118px;line-height:1;color:var(--blue);letter-spacing:-2px;white-space:nowrap}
.opening-date small{font-size:80px}
.preview{position:absolute;top:170px;left:38px;display:flex;align-items:center;gap:16px;white-space:nowrap}
.preview-label{background:var(--green);color:var(--white);font-weight:700;font-size:22px;padding:4px 12px;border-radius:4px}
.preview-dates{font-family:"M PLUS Rounded 1c",sans-serif;font-weight:800;font-size:34px;color:var(--blue)}
.preview-dates small{font-size:22px}
.preview-note{position:absolute;top:168px;left:618px;width:230px;font-size:12.5px;line-height:1.5;color:var(--ink)}
.clinic-mark{position:absolute;top:248px;left:520px;width:300px;text-align:center}
.clinic-mark .square{display:block;width:78px;height:78px;margin:0 auto 14px;background:var(--blue-soft);border-radius:10px}
.clinic-mark .name{font-weight:700;font-size:24px;color:var(--blue);white-space:nowrap}
.clinic-mark .roman{font-size:13px;color:var(--blue);margin-top:2px}
.greeting{position:absolute;top:405px;left:440px;width:405px;font-size:13.5px;line-height:1.72;text-align:justify}
.clinic-title{position:absolute;top:610px;left:0;width:100%;text-align:center;font-family:"M PLUS Rounded 1c",sans-serif;font-weight:800;font-size:64px;line-height:1.1;color:var(--blue);letter-spacing:1px;white-space:nowrap}
.title-bar{position:absolute;top:690px;left:40px;width:795px;height:34px;display:flex;gap:6px}
.title-bar span{display:flex;align-items:center;justify-content:center;background:var(--blue);color:var(--white);font-weight:700;font-size:20px}
.title-bar .kind{flex:1.35;letter-spacing:12px}
.title-bar .director{flex:1}
.hours{position:absolute;top:752px;left:40px;width:350px}
.hours-label{display:inline-block;background:var(--green);color:var(--white);font-weight:700;font-size:18px;padding:3px 12px;border-radius:3px}
.hours table{width:100%;border-collapse:collapse;margin-top:12px;font-size:18px;text-align:center}
.hours th{font-weight:700;color:var(--blue);padding:4px 0}
.hours td{padding:6px 0;color:var(--blue);border-top:1px solid var(--blue-soft)}
.hours td.time{background:var(--blue);color:var(--white);font-weight:700;width:120px;white-space:nowrap}
.closed{margin-top:18px;border:2px solid var(--blue);padding:10px 14px;font-size:18px;font-weight:700;color:var(--blue);line-height:1.6;background:var(--blue-pale)}
.contact{position:absolute;top:1040px;left:40px;width:380px;color:var(--blue);font-style:normal}
.contact .address{font-size:17px}
.contact .tel{font-family:"M PLUS Rounded 1c",sans-serif;font-weight:800;font-size:38px;line-height:1.2;white-space:nowrap}
.contact .tel small{font-size:22px}
.contact .url{font-size:16px}
.map{position:absolute;top:752px;left:440px;width:405px;height:405px;background:var(--blue-pale);border:2px solid var(--blue-soft);display:flex;align-items:center;justify-content:center;font-size:16px;color:var(--blue)}
.bottom-rule{position:absolute;left:0;bottom:18px;width:100%;height:6px;background:var(--blue)}
</style>
</head>
<body>
<main class="flyer">
  <h1 class="opening-date">3月24日<small>(月)</small>開院</h1>

  <div class="preview">
    <span class="preview-label">内覧会のご案内</span>
    <span class="preview-dates">3月21日<small>(金)</small>・22日<small>(土)</small></span>
  </div>
  <p class="preview-note">※10:00～16:00まで内覧会を実施いたします。お気軽にご来院ください。</p>

  <div class="clinic-mark">
    <span class="square"></span>
    <div class="name">はるかぜペットクリニック</div>
    <div class="roman">Harukaze Pet Clinic</div>
  </div>

  <p class="greeting">はじめまして、はるかぜペットクリニック院長の森岡健司です。大学卒業後、熊本市内の動物病院で7年間勤務し、2014年3月24日に動物病院を開院することになりました。ホームドクターとして地域の皆様に親しまれる病院であるとともに、飼い主様と一緒に家族である動物たちの最善のケアができるように努めてまいりたいと思います。ワンちゃん達が遊べるスペースも少しですが用意してあります。ぜひ気軽に遊びにいらしてください。今後ともよろしくお願い致します。</p>

  <h2 class="clinic-title">はるかぜペットクリニック</h2>
  <div class="title-bar">
    <span class="kind">動物病院</span>
    <span class="director">院長・森岡健司</span>
  </div>

  <section class="hours">
    <span class="hours-label">診療時間</span>
    <table>
      <tr><th></th><th>月</th><th>火</th><th>水</th><th>木</th><th>金</th><th>土</th></tr>
      <tr><td class="time">9:00～12:00</td><td>●</td><td>●</td><td>●</td><td>●</td><td>●</td><td>●</td></tr>
      <tr><td class="time">15:30～19:30</td><td>●</td><td>●</td><td>●</td><td>●</td><td>●</td><td>★</td></tr>
    </table>
    <div class="closed">★土曜はPM16時まで診療<br>休診日 / 日曜・祝日</div>
  </section>

  <address class="contact">
    <div class="address">熊本市東区青葉台2丁目5-18</div>
    <div class="tel"><small>TEL</small>096-000-4821</div>
    <div class="url">http://harukaze-petclinic.example</div>
  </address>

  <div class="map" role="img" aria-label="クリニックまでの地図">地図スペース</div>

  <div class="bottom-rule"></div>
</main>
</body>
</html>
```